Marrowby's Vacation Rentals Business Card

Multi Million dollar villa rentals in the Dominican Republic.

Industry/Entity Type

Business

Contact Information for Business Card

I am looking for a high-end look around my company name/logo (see attached) on one side incorporating the following info: first and last name, title, address, phone #, email and company website. On the backside I want to add a full color picture of one of our villas (see attached).

```html
<!DOCTYPE html>
<html lang="en">
<head>
<meta charset="utf-8">
<title>Marrowby's Vacation Rentals – Business Card</title>
<link href="https://fonts.googleapis.com/css2?family=Open+Sans:wght@400;600;700&display=swap" rel="stylesheet">
<style>
  :root {
    --backdrop: #8fd0c3;
    --orange-deep: #e8552a;
    --orange-mid: #f26a2a;
    --orange-light: #f7941e;
    --ink: #4a4a4a;
    --paper: #ffffff;
    --photo-light: #9cc8ee;
    --photo-deep: #2d8fd6;
  }
  * { box-sizing: border-box; margin: 0; padding: 0; }
  html, body {
    width: 1200px; height: 1200px; overflow: hidden;
    background: var(--backdrop);
    font-family: "Open Sans", Arial, sans-serif;
  }
  .sheet {
    width: 1200px; height: 1200px;
    display: flex; flex-direction: column;
    align-items: center; justify-content: center; gap: 60px;
  }
  .card {
    width: 820px; height: 469px;
    box-shadow: 0 6px 18px rgba(0,0,0,0.15);
  }
  /* Front */
  .card-front {
    background: linear-gradient(100deg, var(--orange-deep) 0%, var(--orange-mid) 45%, var(--orange-light) 100%);
    padding: 30px 36px;
  }
  .card-front__inner {
    width: 100%; height: 100%;
    background: var(--paper);
    display: flex; align-items: center;
    padding: 0 34px 0 48px;
  }
  .brand {
    flex: 0 0 345px;
    display: flex; align-items: center; gap: 14px;
  }
  .brand__dot {
    width: 40px; height: 40px; border-radius: 50%;
    background: var(--orange-light);
    flex: none;
  }
  .brand__name {
    font-weight: 700; font-size: 30px; line-height: 1.15;
    color: var(--orange-mid);
  }
  .contact { flex: 1; color: var(--ink); }
  .contact__person {
    font-weight: 600; font-size: 17px; letter-spacing: 0.5px;
    text-transform: uppercase; margin-bottom: 12px;
  }
  .contact__list { list-style: none; font-size: 14px; line-height: 1.5; }
  .contact__list li { display: flex; align-items: center; gap: 10px; }
  .contact__list svg { width: 14px; height: 14px; flex: none; }
  .contact__address { font-size: 14px; line-height: 1.4; margin-top: 12px; }
  /* Back */
  .card-back {
    background: var(--paper);
    padding: 24px 30px;
  }
  .villa-photo {
    width: 100%; height: 100%;
    background: linear-gradient(160deg, var(--photo-light) 0%, var(--photo-deep) 100%);
  }
</style>
</head>
<body>
<main class="sheet">
  <section class="card card-front" aria-label="Business card front">
    <div class="card-front__inner">
      <div class="brand">
        <span class="brand__dot"></span>
        <span class="brand__name">Marrowby's Vacation Rentals</span>
      </div>
      <div class="contact">
        <p class="contact__person">Dana Ellery – CEO</p>
        <ul class="contact__list">
          <li>
            <svg viewBox="0 0 14 14" aria-hidden="true"><rect x="3.5" y="1" width="7" height="12" rx="1.5" fill="none" stroke="var(--orange-light)" stroke-width="1.4"/><line x1="6" y1="10.5" x2="8" y2="10.5" stroke="var(--orange-light)" stroke-width="1.4"/></svg>
            +00 11 222 3333
          </li>
          <li>
            <svg viewBox="0 0 14 14" aria-hidden="true"><rect x="1" y="3" width="12" height="8" fill="none" stroke="var(--orange-light)" stroke-width="1.4"/><polyline points="1,3 7,8 13,3" fill="none" stroke="var(--orange-light)" stroke-width="1.4"/></svg>
            dana@marrowbysvacations.com
          </li>
          <li>
            <svg viewBox="0 0 14 14" aria-hidden="true"><circle cx="7" cy="7" r="5.8" fill="none" stroke="var(--orange-light)" stroke-width="1.3"/><ellipse cx="7" cy="7" rx="2.5" ry="5.8" fill="none" stroke="var(--orange-light)" stroke-width="1.1"/><line x1="1.2" y1="7" x2="12.8" y2="7" stroke="var(--orange-light)" stroke-width="1.1"/></svg>
            www.marrowbysvacations.com
          </li>
        </ul>
        <p class="contact__address">#14, Solano Bldg, Dominican Republic<br>orum imus ex et, apellab ipsapid esti<br>odicietusci a es exerovitis.</p>
      </div>
    </div>
  </section>

  <section class="card card-back" aria-label="Business card back">
    <div class="villa-photo" role="img" aria-label="Full colour photograph of a company villa with its pool"></div>
  </section>
</main>
</body>
</html>
```